Vorna Fleet business card

I am needing a business card that at a glance shows all the services that we provide emphasizing some more than others. We are a Fleet and Compliance management company as well as a software company. We provide outsourced solutions for KPX compliance and HR services via our own software.
In addition, we do
drug testing
GPS
Cameras
Electronic DVIRS
ELD's

Target Market(s)

Transportation company owners

Industry/Entity Type

Transportation supplier

Contact Information for Business Card

the card should inform potential customers what we do

Other font styles liked:
• I have added brand guidelines. See attached

Requirements
Must have
• See description
Should not have
• Colors outside my brand guide. See attached

```html
<!DOCTYPE html>
<html lang="en">
<head>
<meta charset="UTF-8">
<title>Vorna Fleet business card</title>
<link href="https://fonts.googleapis.com/css2?family=Montserrat:wght@500;600;700;800&family=Roboto+Condensed:wght@400;700&display=swap" rel="stylesheet">
<style>
  :root {
    --bg: #8a8a8a;
    --card-white: #ffffff;
    --card-dark: #1f1f20;
    --ink: #111111;
    --red: #ee1c2b;
    --muted-logo: #3b3b3d;
    --light-text: #e6e6e6;
  }
  * { box-sizing: border-box; margin: 0; padding: 0; }
  html, body { width: 1200px; height: 800px; overflow: hidden; }
  body {
    background: var(--bg);
    font-family: "Montserrat", sans-serif;
    display: flex;
    align-items: center;
    justify-content: center;
    gap: 40px;
  }
  .card {
    width: 560px;
    height: 320px;
    position: relative;
    overflow: hidden;
    box-shadow: 0 14px 30px rgba(0,0,0,0.3);
  }

  /* Front */
  .card-front { background: var(--card-white); }
  .front-main {
    position: absolute;
    top: 0; left: 0; right: 0;
    height: 262px;
    display: flex;
    align-items: center;
    justify-content: center;
    gap: 26px;
  }
  .person { text-align: right; }
  .person-name {
    font-weight: 700;
    font-size: 26px;
    letter-spacing: 0.5px;
    color: var(--ink);
    line-height: 1;
  }
  .person-title {
    font-weight: 600;
    font-size: 15px;
    letter-spacing: 1px;
    color: var(--red);
    margin-top: 6px;
  }
  .divider {
    width: 1px;
    height: 92px;
    background: var(--ink);
  }
  .brand-name {
    font-weight: 800;
    font-size: 30px;
    color: var(--ink);
    line-height: 1.05;
  }
  .contact-band {
    position: absolute;
    left: 0; right: 0; bottom: 0;
    height: 58px;
    display: flex;
    font-size: 13px;
    font-weight: 500;
    color: #ffffff;
  }
  .contact-item {
    display: flex;
    align-items: center;
    justify-content: center;
    gap: 8px;
  }
  .contact-phone { background: var(--ink); width: 34%; }
  .contact-email { background: var(--red); width: 36%; font-size: 14px; }
  .contact-web { background: var(--ink); width: 30%; font-size: 12px; }
  .contact-icon { width: 12px; height: 12px; flex: none; }

  /* Back */
  .card-back { background: var(--card-dark); }
  .back-brand {
    position: absolute;
    top: 70px; left: 0; right: 0;
    text-align: center;
    font-weight: 800;
    font-size: 54px;
    color: var(--muted-logo);
    letter-spacing: 1px;
  }
  .tagline-row {
    position: absolute;
    top: 196px; left: 0; right: 0;
    display: flex;
    align-items: center;
    justify-content: center;
    gap: 10px;
  }
  .tagline-rule { width: 70px; height: 2px; background: var(--red); }
  .tagline {
    font-weight: 800;
    font-size: 15px;
    letter-spacing: 0.5px;
    color: var(--red);
  }
  .services {
    position: absolute;
    top: 232px; left: 0; right: 0;
    text-align: center;
    font-family: "Roboto Condensed", sans-serif;
    font-size: 14.5px;
    color: var(--light-text);
    word-spacing: 1px;
  }
  .services .sep { margin: 0 4px; }
</style>
</head>
<body>

  <section class="card card-front">
    <div class="front-main">
      <div class="person">
        <p class="person-name">DALE MORROW</p>
        <p class="person-title">CEO</p>
      </div>
      <div class="divider"></div>
      <p class="brand-name">Vorna<br>Fleet</p>
    </div>
    <div class="contact-band">
      <div class="contact-item contact-phone">
        <svg class="contact-icon" viewBox="0 0 24 24" aria-hidden="true"><path fill="#fff" d="M6.6 10.8a15.1 15.1 0 0 0 6.6 6.6l2.2-2.2a1 1 0 0 1 1-.25 11.4 11.4 0 0 0 3.6.57 1 1 0 0 1 1 1V20a1 1 0 0 1-1 1A17 17 0 0 1 3 4a1 1 0 0 1 1-1h3.5a1 1 0 0 1 1 1c0 1.25.2 2.45.57 3.57a1 1 0 0 1-.25 1z"/></svg>
        <span>(555) 014-2870</span>
      </div>
      <div class="contact-item contact-email">
        <svg class="contact-icon" viewBox="0 0 24 24" aria-hidden="true"><rect x="2" y="5" width="20" height="14" fill="#fff"/><path d="M2 5l10 8 10-8" fill="none" stroke="#ee1c2b" stroke-width="2"/></svg>
        <span>info@vornafleet.com</span>
      </div>
      <div class="contact-item contact-web">
        <svg class="contact-icon" viewBox="0 0 24 24" aria-hidden="true"><circle cx="12" cy="12" r="9" fill="none" stroke="#fff" stroke-width="2"/><path d="M3 12h18M12 3c3 3 3 15 0 18M12 3c-3 3-3 15 0 18" fill="none" stroke="#fff" stroke-width="1.6"/></svg>
        <span>www.vornafleet.com</span>
      </div>
    </div>
  </section>

  <section class="card card-back">
    <p class="back-brand">Vorna Fleet</p>
    <div class="tagline-row">
      <span class="tagline-rule"></span>
      <p class="tagline">COMPLIANCE MADE SIMPLE</p>
      <span class="tagline-rule"></span>
    </div>
    <p class="services">
      Compliance<span class="sep">|</span>Fleet Management<span class="sep">|</span>Drug testing<span class="sep">|</span>GPS<span class="sep">|</span>Cameras<span class="sep">|</span>Electronic DVIRS<span class="sep">|</span>ELD's
    </p>
  </section>

</body>
</html>
```